Lanterns Over The Quiet Meadow Waters Book Cover

Book cover for a new book titled "Lanterns Over The Quiet Meadow Waters" which will show how retirees can pay NO tax in their retirement. Would like you to use your creative inspiration to come up with a design.

Please make MEADOW WATERS the emphasis of the title.

can you show money being rescued, or freed, from taxes.

I'm trying convey the message that retirees can FREE themselves from the burden of taxes in retirement by reading this book and following the instructions. Think about a person swimming with a weight on his back, sinking him. Suddenly the weight is removed. The feeling and imagery of the load being light now

Doing MEADOW WATERS can alleviate many of unnecessary taxes which will weight retirees down. But, unfortunately, many advisors in my industry do not educate their clients on this stuff.

Not a fan of dark backgrounds, generally speaking. Lighter is good.

Remember folks, go to brindlecart. Type in Roth IRA books. what will jump out over the stuff that's already there? Thanks!

Target Market(s)

recent, or soon to be, retirees, people in their 50s and 60s, typically couples

Industry/Entity Type

Financial

Font styles to use
Serif

Colors

Designer to choose colors to be used in the design.

Requirements
Must have
• Be optimistic, sunny, happy. How you do that? I don't know, that's why I'm hiring you. This book is designed for the lay person, (average Joe and Jane)
• Put my picture on the lower back.
• My name at bottom of the cover
Nice to have
• Be nice to have the cover POP on Brindlecart because I'm competing with so many other books and thumbnails
• Maybe a kite with a dollar bill that is breaking from a ball and chain? Just an idea.
Should not have
• No guys in suits. Happy couples sitting on the beach or sailing. That stuff is in every piece of financial planning literature.
• NOT TECHNICAL. NO PIGGY BANKS Design please

```html
<!DOCTYPE html>
<html lang="en">
<head>
<meta charset="utf-8">
<title>Lanterns Over The Quiet Meadow Waters — Book Cover</title>
<link rel="stylesheet" href="https://fonts.googleapis.com/css2?family=Bebas+Neue&family=Oswald:wght@600;700&family=Montserrat:wght@500;600&display=swap">
<style>
  :root {
    --stage: #e9e9ea;
    --cover-top: #ffffff;
    --cover-mid: #e6e6e7;
    --cover-bottom: #a7a8aa;
    --ink: #141414;
    --title-blue-light: #3f8fd6;
    --title-blue-dark: #0b3a73;
    --band-blue: #1d5ba6;
    --band-text: #ffffff;
    --art-light: #d7e2cf;
    --art-mid: #b99a80;
    --art-dark: #8b6f5a;
  }

  * { margin: 0; padding: 0; box-sizing: border-box; }

  html, body {
    width: 1200px;
    height: 1200px;
    overflow: hidden;
    background: var(--stage);
  }

  .canvas {
    position: relative;
    width: 1200px;
    height: 1200px;
    background: radial-gradient(ellipse at 50% 40%, #f6f6f7 0%, var(--stage) 70%);
  }

  .book-cover {
    position: absolute;
    left: 240px;
    top: 60px;
    width: 720px;
    height: 1080px;
    overflow: hidden;
    background: linear-gradient(180deg,
      var(--cover-top) 0%,
      var(--cover-top) 30%,
      var(--cover-mid) 55%,
      var(--cover-bottom) 100%);
    box-shadow: 0 18px 40px rgba(0, 0, 0, 0.18);
  }

  .cover-title {
    position: absolute;
    left: 0;
    top: 0;
    width: 720px;
    height: 640px;
  }

  .cover-title .title-lead {
    font-family: "Oswald", "Bebas Neue", sans-serif;
    font-weight: 700;
    font-size: 88px;
    fill: var(--ink);
  }

  .cover-title .title-emphasis {
    font-family: "Bebas Neue", "Oswald", sans-serif;
    font-size: 330px;
  }

  .cover-title .title-tail {
    font-family: "Bebas Neue", "Oswald", sans-serif;
    font-size: 158px;
    fill: var(--ink);
  }

  .cover-art {
    position: absolute;
    left: 150px;
    top: 640px;
    width: 420px;
    height: 330px;
    border-radius: 46% 54% 10px 10px / 40% 40% 10px 10px;
    background:
      radial-gradient(ellipse 60% 38% at 56% 26%, var(--art-light) 0%, rgba(215, 226, 207, 0) 100%),
      radial-gradient(ellipse 28% 70% at 46% 78%, var(--art-mid) 0%, rgba(185, 154, 128, 0) 100%),
      linear-gradient(180deg, rgba(139, 111, 90, 0) 40%, rgba(139, 111, 90, 0.25) 100%);
  }

  .author-band {
    position: absolute;
    left: 0;
    bottom: 0;
    width: 720px;
    height: 116px;
    background: var(--band-blue);
    display: flex;
    align-items: center;
    justify-content: center;
  }

  .author-name {
    font-family: "Montserrat", sans-serif;
    font-weight: 500;
    font-size: 54px;
    letter-spacing: 4px;
    color: var(--band-text);
    text-transform: uppercase;
    white-space: nowrap;
  }
</style>
</head>
<body>
  <main class="canvas">
    <article class="book-cover">
      <svg class="cover-title" viewBox="0 0 720 640" role="img"
           aria-label="Lanterns Over The Quiet Meadow Waters">
        <defs>
          <linearGradient id="emphasis-blue" x1="0" y1="0" x2="0" y2="1">
            <stop offset="0" stop-color="var(--title-blue-light)"/>
            <stop offset="0.55" stop-color="#2467ad"/>
            <stop offset="1" stop-color="var(--title-blue-dark)"/>
          </linearGradient>
        </defs>
        <text class="title-lead" x="60" y="168" textLength="600" lengthAdjust="spacingAndGlyphs">Lanterns Over The Quiet</text>
        <text class="title-emphasis" x="52" y="462" textLength="616" lengthAdjust="spacingAndGlyphs" fill="url(#emphasis-blue)">MEADOW</text>
        <text class="title-tail" x="60" y="606" textLength="600" lengthAdjust="spacingAndGlyphs">WATERS</text>
      </svg>

      <div class="cover-art" role="img"
           aria-label="Photograph of a hand launching a paper airplane folded from a dollar bill"></div>

      <footer class="author-band">
        <p class="author-name">Dale Whitcombe</p>
      </footer>
    </article>
  </main>
</body>
</html>
```